Voltarey - Flyer design

Description -
Motorhome and Caravan EWOFs
Recreational Vehicles (such as caravans, motorhomes, RVs, Boats etc) and Relocatable buildings that can be connected to an electricity supply must be regularly checked for electrical safety. An EWOF needs to be issued every 4 years.
Pre-purchase house inspections
A pre-purchase electrical inspection prior to buying a home can be used to identify any dangerous and unsafe electrical parts of the installation that may be costly to repair once the property has been purchased. Giving you peace of mind when buying your new home.
High risk Electrical inspections
All Prescribed Electrical Work that falls under the High Risk category must be inspected by a Registered Electrical Inspector and have a Record of Inspection certificate issued.
Electric Vehicle Chargers
Any electrical vehicle charger that can be accessed by the public (ie in a non-domestic situation) must be periodically inspected and certified every 12 months.
General Electrical Services
Domestic and commercial - We do new builds, Renovations, Maintenance and more!
Dean Fowler - Electrician and Electrical Inspector
Ph - 0227839152
Dean@voltarey.co.nz
Auckland
------
I also want there to be a few symbols similar to the files I have attached.
The main areas that I am hoping to find work is with caravans/motohomes and EV car chargers so these symbols are quite important.
Thanks so much

```html
<!DOCTYPE html>
<html lang="en">
<head>
<meta charset="utf-8">
<title>Voltarey – Electrical Inspection Flyer</title>
<link rel="stylesheet" href="https://fonts.googleapis.com/css2?family=Anton&family=Antonio:wght@400;500;700&family=Barlow+Condensed:wght@400;600&display=swap">
<style>
  :root{
    --navy:#1f2a5c;
    --navy-deep:#19204a;
    --yellow:#f5d327;
    --gold:#f2a91c;
    --white:#ffffff;
    --panel-top:rgba(62,72,104,0.62);
  }
  *{margin:0;padding:0;box-sizing:border-box;}
  html,body{width:849px;height:1200px;overflow:hidden;background:var(--navy);}
  .flyer{position:relative;width:849px;height:1200px;background:var(--navy);overflow:hidden;}
  .hero-photo{position:absolute;left:0;top:0;width:849px;height:466px;
    background:linear-gradient(180deg,#b9b7b1 0%,#c9c2b3 40%,#8d8f99 52%,#b08d52 62%,#c29c5c 80%,#a49a8c 100%);}
  .side-panel{position:absolute;left:30px;top:28px;width:328px;height:1141px;
    background:linear-gradient(180deg,var(--panel-top) 0,var(--panel-top) 438px,var(--navy-deep) 438px);}
  .headline{position:absolute;right:521px;top:52px;text-align:right;
    font-family:"Anton",sans-serif;font-weight:400;color:var(--yellow);font-size:78px;line-height:80.6px;
    text-transform:uppercase;transform:scaleX(1.3);transform-origin:right top;}
  .tagline{position:absolute;right:521px;top:494px;text-align:right;white-space:nowrap;
    font-family:"Antonio",sans-serif;font-weight:500;color:var(--white);font-size:33px;line-height:43px;}
  .contact{position:absolute;left:88px;width:250px;color:var(--white);font-family:"Antonio",sans-serif;white-space:nowrap;}
  .contact-name{top:918px;font-size:60px;font-weight:700;line-height:66px;}
  .contact-role{top:987px;font-size:19px;font-weight:400;line-height:24px;}
  .contact-phone{top:1016px;font-size:42px;font-weight:700;color:var(--yellow);line-height:52px;}
  .contact-email{top:1068px;font-size:29px;font-weight:400;line-height:36px;}
  .contact-city{top:1112px;font-size:21px;font-weight:400;line-height:28px;}
  .services{list-style:none;}
  .service{position:absolute;left:380px;width:420px;}
  .service-icon{position:absolute;left:0;width:90px;height:90px;border-radius:50%;
    background:radial-gradient(circle at 35% 30%,#f7b733,var(--gold) 70%,#e2961a);}
  .service-icon svg{width:90px;height:90px;}
  .service-body{position:absolute;left:111px;width:303px;}
  .service-title{font-family:"Barlow Condensed",sans-serif;font-weight:600;color:var(--yellow);
    font-size:21px;line-height:24px;text-transform:uppercase;white-space:nowrap;}
  .service-text{font-family:"Barlow Condensed",sans-serif;font-weight:400;color:var(--white);
    font-size:17px;line-height:21.8px;text-align:justify;}
</style>
</head>
<body>
<main class="flyer">
  <div class="hero-photo" role="img" aria-label="Photo of a white motorhome with flames and smoke coming from its side window, parked on a dry grass plain under a cloudy sky"></div>
  <div class="side-panel"></div>

  <h1 class="headline">Trust<br>me you<br>don’t<br>want<br>this!</h1>

  <p class="tagline">I offer a certified<br>electrical inspection<br>of your caravan for<br>your peace of mind.</p>

  <div class="contact contact-name">Dean Fowler</div>
  <div class="contact contact-role">Electrician and Electrical Inspector</div>
  <div class="contact contact-phone">Ph - 0227839152</div>
  <div class="contact contact-email">Dean@voltarey.co.nz</div>
  <div class="contact contact-city">Auckland</div>

  <ul class="services">
    <li class="service" style="top:497px">
      <div class="service-icon" style="top:5px">
        <svg viewBox="0 0 90 90" fill="none" stroke="#1f2a5c" stroke-width="2.6" stroke-linejoin="round" stroke-linecap="round">
          <path d="M24 56 V38 Q24 30 34 30 H58 Q68 30 70 42 L72 56 Z"/>
          <rect x="31" y="37" width="8" height="15"/>
          <rect x="50" y="36" width="14" height="7" rx="1"/>
          <circle cx="60" cy="58" r="5"/>
          <path d="M24 56 H16 M12 56 H16 V62"/>
        </svg>
      </div>
      <div class="service-body">
        <h2 class="service-title">Motorhome and Caravan EWOFs</h2>
        <p class="service-text">Recreational Vehicles (such as caravans, RVs, motorhomes, Boats etc) and Relocatable buildings that can be connected to an electricity supply must be regularly checked for electrical safety. An EWOF needs to be issued every 4 years.</p>
      </div>
    </li>
    <li class="service" style="top:653px">
      <div class="service-icon" style="top:5px">
        <svg viewBox="0 0 90 90" fill="none" stroke="#1f2a5c" stroke-width="2.6" stroke-linejoin="round" stroke-linecap="round">
          <rect x="27" y="18" width="36" height="52" rx="3"/>
          <rect x="32" y="23" width="26" height="15" rx="1"/>
          <path d="M36 35 Q45 26 54 35 M45 36 L49 29"/>
          <circle cx="45" cy="53" r="8"/>
          <path d="M40 58 L50 48"/>
          <path d="M27 40 H20 V60 H27 M63 40 H70 V60 H63"/>
        </svg>
      </div>
      <div class="service-body">
        <h2 class="service-title">Pre-purchase House Inspections</h2>
        <p class="service-text">A pre-purchase electrical inspection prior to buying a home can be used to identify any dangerous and unsafe electrical parts of the installation that may be costly to repair once the property has been purchased. Giving you peace of mind when buying your new home.</p>
      </div>
    </li>
    <li class="service" style="top:831px">
      <div class="service-icon" style="top:3px">
        <svg viewBox="0 0 90 90" fill="none" stroke="#1f2a5c" stroke-width="2.6" stroke-linejoin="round" stroke-linecap="round">
          <circle cx="60" cy="26" r="8"/>
          <path d="M56 34 V40 H64 V34 M60 12 V9 M70 18 L73 15 M50 18 L47 15 M74 26 H77"/>
          <rect x="22" y="40" width="30" height="36" rx="3"/>
          <rect x="27" y="45" width="20" height="10" rx="1"/>
          <circle cx="37" cy="65" r="5"/>
          <path d="M52 58 H60 V74"/>
        </svg>
      </div>
      <div class="service-body">
        <h2 class="service-title">High Risk Electrical Inspections</h2>
        <p class="service-text">All Prescribed Electrical Work that falls under the High Risk category must be inspected by a Registered Electrical Inspector and have a Record of Inspection certificate issued.</p>
      </div>
    </li>
    <li class="service" style="top:966px">
      <div class="service-icon" style="top:-2px">
        <svg viewBox="0 0 90 90" fill="none" stroke="#1f2a5c" stroke-width="2.6" stroke-linejoin="round" stroke-linecap="round">
          <circle cx="45" cy="45" r="30"/>
          <path d="M27 52 V45 L33 35 Q35 32 40 32 H52 Q56 32 58 36 L63 45 V52 Z"/>
          <circle cx="35" cy="54" r="4"/>
          <circle cx="55" cy="54" r="4"/>
          <path d="M47 35 L42 43 H48 L43 50"/>
          <path d="M22 24 L14 16 M18 20 L24 14 M22 24 L28 18"/>
        </svg>
      </div>
      <div class="service-body">
        <h2 class="service-title">Electric Vehicle Chargers</h2>
        <p class="service-text">Any electrical vehicle charger that can be accessed by the public (ie in a non-domestic situation) must be periodically inspected and certified every 12 months.</p>
      </div>
    </li>
    <li class="service" style="top:1101px">
      <div class="service-body">
        <h2 class="service-title">General Electrical Services</h2>
        <p class="service-text">Domestic and commercial - We do new builds, Renovations, Maintenance and more!</p>
      </div>
    </li>
  </ul>
</main>
</body>
</html>
```